Industrial Services company needs a business card design

We provide industrial maintenance services including sandblasting, painting, pressure washing, storage tank rehabilitation, and welding. I would like an industrial design that's eye catching. I would like the back-side of the card to list our services.

Industry/Entity Type

Construction

Contact Information for Business Card

address: 418 Hartwell Lane, York, PA 17405
Phone: 410-637-4815
email: corvethinc@mailbrook.net
Daniel Verhoeven, President
www.corvethcoating.net

Logo Text

Corveth Industrial Services

Font styles to use
Sans Serif

Colors
000000
229ed3
0692cd
ffffff

Requirements
Must have
• Easy to read
• our services listed/included on back of card
• eye catching color combinations
Nice to have
• Water storage tank image

```html
<!DOCTYPE html>
<html lang="en">
<head>
<meta charset="utf-8">
<title>Corveth Inc. – Business Card</title>
<link href="https://fonts.googleapis.com/css2?family=Jost:ital,wght@0,400;0,500;1,500&family=Oswald:wght@700&display=swap" rel="stylesheet">
<style>
  :root {
    --ink: #000000;
    --blue-light: #229ed3;
    --blue-deep: #0692cd;
    --blue-back: #35a7dc;
    --blue-dot: #0477ae;
    --teal-dark: #16404f;
    --white: #ffffff;
    --page: #e6e6e6;
  }
  * { margin: 0; padding: 0; box-sizing: border-box; }
  html, body { width: 993px; height: 1200px; overflow: hidden; }
  body { background: var(--page); font-family: "Jost", sans-serif; position: relative; }
  .card { position: absolute; left: 36px; width: 931px; height: 558px; background: var(--white); overflow: hidden; }
  .card--front { top: 31px; }
  .card--back { top: 607px; left: 31px; }
  .band { position: absolute; left: 0; width: 467px; height: 27px; background: var(--blue-light); }
  .band--top { top: 0; }
  .band--bottom { bottom: 0; background: var(--blue-deep); }
  .abs { position: absolute; white-space: nowrap; }

  /* front */
  .contact-panel { position: absolute; left: 467px; top: 27px; width: 464px; height: 504px; background: var(--blue-deep); }
  .dot { position: absolute; left: -12px; width: 28px; height: 28px; border-radius: 50%; background: var(--blue-dot); }
  .contact-label, .contact-value { position: absolute; left: 35px; color: var(--white); font-size: 19px; line-height: 22px; font-weight: 500; white-space: nowrap; }
  .contact-value { font-weight: 400; }
  .mini-logo { position: absolute; left: 35px; font-family: "Oswald", sans-serif; font-weight: 700; font-size: 25px; line-height: 28px; color: var(--white); white-space: nowrap; }
  .logo { font-family: "Oswald", sans-serif; font-weight: 700; }
  .logo--front { left: 30px; top: 103px; font-size: 80px; line-height: 80px; color: var(--blue-light); transform: scaleX(0.84); transform-origin: left center; }
  .tagline { font-style: italic; font-weight: 500; color: var(--teal-dark); }
  .tagline--front { left: 30px; top: 199px; font-size: 24px; line-height: 28px; }
  .identity { position: absolute; left: 0; width: 467px; text-align: center; white-space: nowrap; }
  .name { top: 312px; font-size: 42px; line-height: 46px; font-weight: 500; color: var(--ink); }
  .role { top: 364px; font-size: 38px; line-height: 44px; font-weight: 500; color: var(--blue-light); }
  .front-phone { top: 446px; font-size: 27px; line-height: 32px; color: #222; }
  .front-email { top: 483px; font-size: 26px; line-height: 32px; color: #222; }

  /* back */
  .back-field { position: absolute; left: 0; top: 27px; width: 931px; height: 504px; background: var(--blue-back); }
  .illustration { position: absolute; left: 72px; top: 4px; width: 800px; height: 460px; border-radius: 40px;
    background: radial-gradient(ellipse at 35% 55%, rgba(40,110,160,0.35), rgba(53,167,220,0) 65%); }
  .back-center { position: absolute; left: 0; width: 931px; text-align: center; white-space: nowrap; }
  .logo--back { top: 37px; font-size: 84px; line-height: 96px; color: var(--white); transform: scaleX(0.86); transform-origin: center; }
  .tagline--back { top: 142px; font-size: 27px; line-height: 30px; }
  .intro { top: 180px; font-size: 34.5px; line-height: 40px; color: #111; }
  .services { top: 221px; list-style: none; color: var(--white); font-size: 35px; line-height: 43.5px; }
  .back-footer { top: 490px; font-size: 21px; line-height: 24px; color: var(--white); }
  .back-footer .sep { margin: 0 24px; }
</style>
</head>
<body>

<section class="card card--front" aria-label="Front of card">
  <div class="band band--top"></div>
  <div class="band band--bottom"></div>

  <div class="abs logo logo--front">CORVETH INC.</div>
  <div class="abs tagline tagline--front">Commercial &amp; Industrial Painting</div>

  <div class="identity name">Daniel Verhoeven</div>
  <div class="identity role">President</div>
  <div class="identity front-phone">Phone: 410-637-4815</div>
  <div class="identity front-email">email: corvethinc@mailbrook.net</div>

  <div class="contact-panel">
    <span class="dot" style="top:28px"></span>
    <span class="contact-label" style="top:34px">Phone:</span>
    <span class="contact-value" style="top:61px">410-637-4815</span>

    <span class="dot" style="top:152px"></span>
    <span class="contact-label" style="top:158px">Email:</span>
    <span class="contact-value" style="top:186px">corvethinc@mailbrook.net</span>

    <span class="dot" style="top:276px"></span>
    <span class="contact-label" style="top:284px">Web:</span>
    <span class="contact-value" style="top:312px">www.corvethcoating.net</span>

    <span class="dot" style="top:392px"></span>
    <span class="mini-logo" style="top:396px">CORVETH INC.</span>
    <span class="contact-label" style="top:433px">Address:</span>
    <span class="contact-value" style="top:460px">418 Hartwell Lane, York, PA 17405</span>
  </div>
</section>

<section class="card card--back" aria-label="Back of card">
  <div class="band band--top"></div>
  <div class="band band--bottom"></div>
  <div class="back-field">
    <div class="illustration" role="img" aria-label="Faint illustration of a maintenance worker holding a wrench beside a water tank"></div>
  </div>

  <div class="back-center logo logo--back">CORVETH INC.</div>
  <div class="back-center tagline tagline--back">Commercial &amp; Industrial Painting</div>
  <p class="back-center intro">We provide industrial maintenance services including</p>
  <ul class="back-center services">
    <li>Sandblasting</li>
    <li>Painting</li>
    <li>Pressure washing</li>
    <li>Storage tank rehabilitation, and</li>
    <li>Welding</li>
  </ul>
  <p class="back-center back-footer">Phone: 410-637-4815<span class="sep">|</span>email: corvethinc@mailbrook.net<span class="sep">|</span>www.corvethcoating.net</p>
</section>

</body>
</html>
```